Service business needs Business Card Design

Looking to create a new business card design that is both professional and unique the can highlight the many services we offer throughout the seasons. Our tagline is "The Steadfast Touch"
Licensed & Insured: PA392617 has to be small and on the back side of the card.
On the Front:
FirstName LastName
Title
We offer the following services:
Deck Repair and Maintenance
Deck Cleaning and Staining/Painting
Power Washing/House Washing
Landscape Lighting Installation
Christmas Lighting Installation

```html
<!DOCTYPE html>
<html lang="en">
<head>
<meta charset="utf-8">
<title>Harborline Services – Business Cards</title>
<link rel="stylesheet" href="https://fonts.googleapis.com/css2?family=Montserrat:wght@400;500;600;700&display=swap">
<style>
  :root{
    --navy:#0b5ea8;
    --navy-deep:#0a4f8f;
    --sky:#4fb6ea;
    --ink:#1f2a36;
    --paper:#ffffff;
    --stage:#e9ecef;
  }
  *{box-sizing:border-box;margin:0;padding:0}
  html,body{width:1200px;height:786px;overflow:hidden}
  body{background:var(--stage);font-family:"Montserrat",sans-serif;position:relative}
  .card{position:absolute;top:238px;width:540px;height:310px;background:var(--paper);
        box-shadow:0 6px 18px rgba(0,0,0,.18);overflow:hidden}
  .card--contact{left:40px}
  .card--services{left:620px}
  .card-bg{position:absolute;inset:0}
  .brand{position:absolute;display:flex;align-items:center;gap:10px;color:var(--navy);font-weight:600}
  .brand-dot{width:34px;height:34px;border-radius:50%;background:var(--navy)}
  .brand-name{display:flex;flex-direction:column;line-height:1}
  .brand-name .word{font-size:30px;letter-spacing:1px}
  .brand-name .sub{font-size:11px;letter-spacing:9.5px;margin-top:5px}
  .card--contact .brand{right:40px;top:42px}
  .card--services .brand{left:150px;top:38px}
  .rule{position:absolute;left:122px;right:38px;top:132px;height:1.5px;background:var(--navy)}
  .person{position:absolute;left:34px;top:168px}
  .person-name{font-size:23px;font-weight:700;color:var(--navy)}
  .person-title{font-size:13px;color:var(--ink);margin-top:1px}
  .person-rule{width:170px;height:1px;background:var(--navy);margin:8px 0 6px}
  .contacts{list-style:none;font-size:12.5px;color:var(--ink)}
  .contacts li{display:flex;align-items:center;gap:10px;height:18px}
  .contacts svg{width:12px;height:12px;fill:var(--navy);flex:none}
  .address{position:absolute;right:34px;top:176px;font-size:12.5px;color:var(--ink);line-height:1.3;text-align:left}
  .license{position:absolute;right:28px;bottom:14px;font-size:12px;color:#fff;font-weight:500}
  .tagline-tab{position:absolute;left:192px;top:138px;width:206px;text-align:center;
               font-size:12.5px;font-weight:600;color:#fff}
  .services{position:absolute;top:200px;list-style:none;color:#fff;font-size:12.5px;line-height:1.6}
  .services li::before{content:"";display:inline-block;width:5px;height:5px;border-radius:50%;
                       background:#fff;margin-right:8px;vertical-align:middle}
  .services--left{left:34px}
  .services--right{left:318px;top:190px}
</style>
</head>
<body>

<section class="card card--contact">
  <svg class="card-bg" viewBox="0 0 540 310" aria-hidden="true">
    <path d="M0,286 L290,286 C308,286 312,252 335,252 L540,252 L540,310 L0,310 Z" fill="var(--sky)"/>
    <path d="M0,294 L300,294 C318,294 322,260 345,260 L540,260 L540,310 L0,310 Z" fill="var(--paper)"/>
    <path d="M0,302 L540,302 L540,310 L0,310 Z" fill="var(--sky)"/>
    <path d="M318,310 C330,300 336,262 360,262 L540,262 L540,310 Z" fill="var(--navy)"/>
  </svg>
  <div class="brand">
    <span class="brand-dot"></span>
    <span class="brand-name"><span class="word">HARBORLINE</span><span class="sub">SERVICES</span></span>
  </div>
  <div class="rule"></div>
  <div class="person">
    <p class="person-name">Daniel Foster</p>
    <p class="person-title">CEO &amp; Founder</p>
    <div class="person-rule"></div>
    <ul class="contacts">
      <li><svg viewBox="0 0 24 24"><path d="M6.6 10.8a15 15 0 0 0 6.6 6.6l2.2-2.2c.3-.3.7-.4 1-.2 1.1.4 2.3.6 3.6.6.6 0 1 .4 1 1V20c0 .6-.4 1-1 1A17 17 0 0 1 3 4c0-.6.4-1 1-1h3.5c.6 0 1 .4 1 1 0 1.3.2 2.5.6 3.6.1.3 0 .7-.2 1z"/></svg>+1 610-555-0148</li>
      <li><svg viewBox="0 0 24 24"><path d="M2 5h20v14H2z M2 5l10 8 10-8" fill="none" stroke="var(--navy)" stroke-width="2"/></svg>info@harborlineservices.com</li>
      <li><svg viewBox="0 0 24 24"><circle cx="12" cy="12" r="10"/></svg>www.harborlineservices.com</li>
    </ul>
  </div>
  <p class="address">48 Meridian Lane, Suite 204<br>Lansdale, PA 19446</p>
  <p class="license">Licensed &amp; Insured: PA392617</p>
</section>

<section class="card card--services">
  <svg class="card-bg" viewBox="0 0 540 310" aria-hidden="true">
    <path d="M0,170 L172,170 L192,132 L398,132 L410,145 L540,145 L540,310 L0,310 Z" fill="var(--sky)"/>
    <path d="M0,178 L178,178 L198,160 L404,160 L416,153 L540,153 L540,310 L0,310 Z" fill="var(--navy)"/>
  </svg>
  <div class="brand">
    <span class="brand-dot"></span>
    <span class="brand-name"><span class="word">HARBORLINE</span><span class="sub">SERVICES</span></span>
  </div>
  <p class="tagline-tab">We offer the services</p>
  <ul class="services services--left">
    <li>Deck Repair and Maintenance</li>
    <li>Deck Cleaning and Staining/Painting</li>
    <li>Power Washing/House Washing</li>
  </ul>
  <ul class="services services--right">
    <li>Landscape Lighting Installation</li>
    <li>Christmas Lighting Installation</li>
  </ul>
</section>

</body>
</html>
```